Flier redesign

Sample fliers are attached from previous 2 years "Seasonal care 2018" and "2019 Seasonal Care" . Need an updated design for this year.

Possible images are attached to this brief. If you use the before/after pictures - you should use both of them. Use images attached to this brief or any from our website that you may prefer.

Colors

Designer to choose colors to be used in the design.

Requirements
Must have
• Colors should match our website theme. www.hollowbrookgardens.org
• Should be a "new" design, not just copying one of the prior year designs with a different image.
• Must be created in photoshop and file must be provided at the end.
• Text should be the same as 2019 version.

```html
<!DOCTYPE html>
<html lang="en">
<head>
<meta charset="utf-8">
<title>2019 Landscaping Packages – Hollowbrook Gardens</title>
<link href="https://fonts.googleapis.com/css2?family=Montserrat:wght@400;500;600&display=swap" rel="stylesheet">
<style>
  :root{
    --maroon:#7b1e34;
    --maroon-text:#8a1d38;
    --card:#efefef;
    --ink:#2b2b2b;
    --white:#ffffff;
    --page:#e2e2e2;
    --gold:#f5c400;
  }
  *{box-sizing:border-box;margin:0;padding:0}
  html,body{width:1200px;height:1200px;overflow:hidden;background:var(--page);
    font-family:"Montserrat",Arial,sans-serif;color:var(--ink)}
  .flyer{position:absolute;left:152px;top:20px;width:896px;height:1160px;overflow:hidden;
    background:#6d8a45}
  .hero-photo{position:absolute;inset:0;
    background:
      radial-gradient(ellipse 60% 35% at 70% 18%, #a9bf5f 0%, rgba(169,191,95,0) 70%),
      radial-gradient(ellipse 50% 30% at 20% 15%, #4f6a2c 0%, rgba(79,106,44,0) 70%),
      linear-gradient(180deg,#5f7b34 0%,#7e9d4a 30%,#8cab55 48%,#6f9140 70%,#557530 100%)}
  .brand-strip{position:absolute;left:50px;top:0;width:223px;height:350px;
    background:linear-gradient(180deg,rgba(255,255,255,.35),rgba(255,255,255,.12))}
  .brand{position:absolute;left:50px;top:0;width:223px;height:49px;background:var(--white);
    display:flex;align-items:center;justify-content:center;gap:8px;
    font-size:14px;font-weight:500;color:var(--maroon);letter-spacing:.5px}
  .brand-dot{width:22px;height:22px;border-radius:50%;border:1.5px solid var(--maroon)}
  .title-seal{position:absolute;left:45px;top:136px;width:230px;height:230px;border-radius:50%;
    border:2px solid rgba(255,255,255,.55);background:rgba(40,50,25,.45);
    display:flex;flex-direction:column;align-items:center;justify-content:center;color:var(--white);text-align:center}
  .title-seal .year{font-size:44px;font-weight:500;line-height:1}
  .title-seal .label{font-size:26px;font-weight:500;line-height:1;margin-top:6px}

  .package{position:absolute;bottom:56px;display:flex;flex-direction:column}
  .package-head{background:var(--maroon);color:var(--white);text-align:center;
    border-radius:50% 50% 0 0 / 100% 100% 0 0;display:flex;flex-direction:column;
    justify-content:flex-end;font-size:19.5px;font-weight:500;line-height:1.28;padding-bottom:12px}
  .package-body{flex:1;background:var(--card);display:flex;flex-direction:column;padding:14px 8px 8px}
  .package-sub{color:var(--maroon-text);font-size:18.5px;font-weight:500;line-height:1.38;text-align:center;margin-bottom:10px}
  .features{list-style:none}
  .features li{position:relative;padding-left:22px;font-size:15.2px;line-height:1.36;margin-bottom:19px}
  .features li::before{content:"";position:absolute;left:0;top:3px;width:13px;height:13px;border:1px solid #444;border-radius:50%}
  .features li::after{content:"";position:absolute;left:4.5px;top:5.5px;width:3px;height:6px;border:solid #444;border-width:0 1.2px 1.2px 0;transform:rotate(45deg)}
  .pricing{margin-top:auto;text-align:center;color:var(--maroon-text)}
  .pricing .term{font-size:19.5px;line-height:1.2}
  .pricing .amount{font-size:27px;font-weight:600;line-height:1.2}
  .pricing .caps{font-size:15.5px;font-weight:600;line-height:1.6}
  .pricing .note{font-size:12.8px;line-height:1.4;margin-top:16px}
  .price-split{display:flex;justify-content:center;margin-top:4px}
  .price-split > div{padding:0 18px}
  .price-split > div + div{border-left:1.5px solid var(--maroon)}

  .seasonal{left:36px;width:251px;top:543px}
  .seasonal .package-head{height:97px;margin:0 3px}
  .basic{left:302px;width:268px;top:481px}
  .basic .package-head{height:101px}
  .perpetual{left:582px;width:276px;top:364px}
  .perpetual .package-head{height:110px;padding-bottom:14px}
  .perpetual .features li{margin-bottom:14px}

  .popular-badge{position:absolute;left:812px;top:408px;width:76px;height:76px;border-radius:50%;
    background:var(--gold);display:flex;align-items:center;justify-content:center}
  .popular-badge span{width:54px;height:54px;border-radius:50%;background:#3a2a10;color:var(--gold);
    font-size:7px;font-weight:600;line-height:1.1;display:flex;align-items:center;justify-content:center;text-align:center}

  .contact-bar{position:absolute;left:0;bottom:0;width:896px;height:56px;background:var(--maroon);
    display:flex;align-items:center;color:var(--white);font-size:17px}
  .contact-bar div{flex:1;text-align:center}
  .contact-bar .sep{flex:0 0 1.5px;height:32px;background:var(--white)}
</style>
</head>
<body>
<main class="flyer">
  <div class="hero-photo" role="img" aria-label="Photograph of a leafy cemetery lawn with rows of headstones and trimmed hedges"></div>
  <div class="brand-strip"></div>
  <div class="brand"><span>HOLLOWBROOK</span><span class="brand-dot"></span><span>GARDENS</span></div>
  <div class="title-seal">
    <div class="year">2019</div>
    <div class="label">LANDSCAPING<br>PACKAGES</div>
  </div>

  <section class="package seasonal">
    <h2 class="package-head">SEASONAL CARE</h2>
    <div class="package-body">
      <p class="package-sub">Seasonal landscaping<br>grave care.</p>
      <ul class="features">
        <li>Weeding and trimming services on your gravesite approximately every 7 weeks during the growing season : mid - April through mid - october</li>
      </ul>
      <div class="pricing">
        <div class="term">3 years</div>
        <div class="amount">$ 345</div>
        <div class="price-split">
          <div><div class="term">2 years</div><div class="amount">$ 230</div></div>
          <div><div class="term">1 years</div><div class="amount">$ 115</div></div>
        </div>
        <p class="note">Multi-year payement locks in current rates.Valid through 10/31/19.</p>
      </div>
    </div>
  </section>

  <section class="package basic">
    <h2 class="package-head">BASIC CARE<br>ENDOWMENT</h2>
    <div class="package-body">
      <p class="package-sub">landscaping care forever<br>for graves with no plantings.</p>
      <ul class="features" style="padding-left:12px">
        <li>Weeding and trimming services on your gravesite 2 times per year : mid - May and mid September</li>
        <li>Monument leveling</li>
        <li>Payment ensures grave care forever</li>
      </ul>
      <div class="pricing">
        <div class="caps">12 MONTHLY<br>PAYMENTS OF</div>
        <div class="term">1 years</div>
        <div class="amount">$ 239</div>
        <p class="note">Call for single payment discount.<br>Valid through 10/31/19.</p>
      </div>
    </div>
  </section>

  <section class="package perpetual">
    <h2 class="package-head">PREPETUAL CARE<br>ENDOWMENT</h2>
    <div class="package-body">
      <p class="package-sub">landscaping care forever<br>for graves with plantings.</p>
      <ul class="features" style="padding-left:6px">
        <li>Weeding and trimming services on your gravesite approximately every 7 weeks during the growing season : mid - April through mid - october</li>
        <li>Monument leveling and cleaning</li>
        <li>Payment ensures grave care forever</li>
        <li>Full bed of boxwood shrubs</li>
        <li>Replacement of shrubs</li>
        <li>Trust certificate</li>
      </ul>
      <div class="pricing">
        <div class="caps">12 MONTHLY<br>PAYMENTS OF</div>
        <div class="term">1 years</div>
        <div class="amount">$ 297</div>
        <p class="note">Call for single payment discount.<br>Valid through 10/31/19.</p>
      </div>
    </div>
  </section>

  <div class="popular-badge"><span>MOST<br>POPULAR</span></div>

  <footer class="contact-bar">
    <div>www.hollowbrookgardens.org</div>
    <span class="sep"></span>
    <div>(555) 214-3080</div>
    <span class="sep"></span>
    <div>www.hollowbrookgardens.org</div>
  </footer>
</main>
</body>
</html>
```